Professional / Luxury Rack Card Design Needed (Do not use AI)

We are a private, boutique style optometry practice in College Station, Texas. We want the new design to communicate a premium, modern, luxury eye care experience while remaining professional and approachable.
When someone picks up this rack card, we want them to think:
"This practice looks modern, advanced, trustworthy, and premium. I would expect exceptional care and a high-end eyewear experience."

Target Market(s)

Families, professionals, adults seeking comprehensive medical eye care and vision correction. Patients seeking premium eyewear, advanced technology, and personalize care. Individuals and families seeking long term relationships with a trusted eye care provider. Patients who value exceptional service, expertise, and convenience.

Industry/Entity Type

Medical & Optometry-luxury optical

Font styles to use
Serif
Other font styles liked:
• Avenir if available. If not, Montserrat for headlines and Open Sans for Body text. For the slogan, use larger bold Montserrat.

Requirements
Must have
• Non-edited photo of doctors (merged together) with names. "Your Vision. Our Focus." Phone, website, Text/Call to Schedule appointment (Call to action to schedule). Accepting new patients. Eye Care center logo prominently displayed. Real photo of Eye Care Center building. Contact information (see attachement with all info)
Nice to have
• For frame brands, use the branded names. (see attachment)
Should not have
• Shouild not be busy/cluttered. Do not use scripted font from my website. Do NOT use AI generated images. Do not edit doctor faces other than merging them together. DO NOT use AI to edit faces....only to merge them side by side.

```html
<!DOCTYPE html>
<html lang="en">
<head>
<meta charset="utf-8">
<title>Brightsight Optical Rack Card</title>
<link rel="stylesheet" href="https://fonts.googleapis.com/css2?family=Playfair+Display:wght@700;800&family=Montserrat:wght@400;500;600;700&family=Open+Sans:wght@400;600;700&display=swap">
<style>
  :root {
    --navy: #263a4f;
    --gold: #d9ad18;
    --white: #ffffff;
    --grey: #6f7275;
    --light: #f1f1f1;
    --ink: #2f3640;
    --page: #dcdcdc;
  }
  * { box-sizing: border-box; margin: 0; padding: 0; }
  html, body { width: 725px; height: 1200px; overflow: hidden; background: var(--page); }
  .sheet { position: relative; width: 725px; height: 1200px; display: flex; gap: 25px; justify-content: center; align-items: center; }
  .card { position: relative; width: 330px; height: 740px; overflow: hidden; box-shadow: 0 6px 18px rgba(0,0,0,.18); }

  /* ---------- front ---------- */
  .front { background: var(--navy); }
  .front-header { position: absolute; inset: 0 0 auto 0; height: 100px; background: var(--white); }
  .brand { position: absolute; left: 32px; top: 26px; display: flex; align-items: center; gap: 10px; }
  .brand-dot { width: 42px; height: 42px; border-radius: 50%; background: var(--grey); flex: none; }
  .brand-name { font-family: "Montserrat", sans-serif; font-weight: 400; font-size: 22px; color: var(--grey); letter-spacing: .5px; line-height: 1; }
  .brand-member { margin-top: 6px; padding-top: 5px; border-top: 1px solid #c9c9c9; font-family: "Montserrat", sans-serif; font-weight: 400; font-size: 8px; letter-spacing: 1.2px; color: var(--grey); text-transform: uppercase; }
  .building-photo { position: absolute; left: 0; top: 100px; width: 100%; height: 175px;
    background: linear-gradient(180deg, #ffffff 0%, #e9dcc3 18%, #bda57e 45%, #7e6a52 70%, var(--navy) 100%); }
  .headline { position: absolute; left: 0; right: 0; top: 258px; text-align: center; font-family: "Playfair Display", serif; font-weight: 800; font-size: 58px; line-height: 61px; color: var(--white); text-shadow: 0 2px 6px rgba(0,0,0,.35); }
  .headline .accent { color: var(--gold); }
  .rule { position: absolute; left: 52px; right: 52px; height: 2px; background: var(--gold); }
  .rule.top { top: 518px; }
  .rule.bottom { top: 677px; }
  .highlights { position: absolute; left: 54px; top: 530px; list-style: none; font-family: "Open Sans", sans-serif; font-size: 15.5px; color: var(--white); line-height: 29px; }
  .highlights li { padding-left: 12px; position: relative; }
  .highlights li::before { content: ""; position: absolute; left: 0; top: 12px; width: 5px; height: 5px; border-radius: 50%; background: var(--gold); }
  .highlights .em { color: var(--gold); font-weight: 700; }
  .highlights .wrap { display: block; line-height: 22px; margin-top: -4px; }
  .contact-row { position: absolute; left: 0; right: 0; top: 690px; display: flex; justify-content: space-around; padding: 0 8px; font-family: "Open Sans", sans-serif; font-size: 9.5px; color: var(--white); text-align: center; }
  .contact-row svg { display: block; margin: 0 auto 3px; width: 10px; height: 10px; fill: var(--gold); }
  .band { position: absolute; left: 0; right: 0; bottom: 0; height: 12px; }

  /* ---------- back ---------- */
  .back { background: var(--white); }
  .doctors { position: absolute; inset: 0 0 auto 0; height: 262px; background: var(--navy); }
  .doctor { position: absolute; width: 120px; text-align: center; font-family: "Open Sans", sans-serif; font-weight: 700; font-size: 8.5px; line-height: 10.5px; color: var(--white); }
  .doctor-photo { width: 81px; height: 81px; margin: 0 auto 6px; border-radius: 50%; border-bottom: 4px solid var(--gold);
    background: radial-gradient(circle at 50% 70%, #f4f4f4 0%, #cbb497 40%, #8d7661 100%); }
  .services { position: absolute; left: 0; right: 0; top: 262px; height: 222px; background: var(--white); }
  .services-title { position: absolute; left: 0; right: 0; top: 16px; text-align: center; font-family: "Playfair Display", serif; font-weight: 800; font-size: 26px; letter-spacing: 1px; color: var(--navy); }
  .service { position: absolute; display: flex; gap: 6px; font-family: "Open Sans", sans-serif; font-size: 10px; line-height: 12px; color: var(--ink); }
  .service .num { flex: none; width: 11px; height: 11px; margin-top: 1px; border-radius: 50%; background: var(--navy); color: var(--white); font-size: 5.5px; font-weight: 700; display: flex; align-items: center; justify-content: center; }
  .brands { position: absolute; left: 0; right: 0; top: 484px; height: 178px; background: var(--light); }
  .brand-grid { position: absolute; left: 10px; right: 10px; top: 12px; display: grid; grid-template-columns: repeat(3, 1fr); row-gap: 18px; text-align: center; font-family: "Montserrat", sans-serif; font-weight: 600; font-size: 12px; letter-spacing: 1.5px; color: #333; text-transform: uppercase; line-height: 19px; }
  .more { position: absolute; left: 0; right: 0; top: 158px; text-align: center; font-family: "Montserrat", sans-serif; font-weight: 600; font-size: 10px; letter-spacing: 2px; color: var(--navy); }
  .info { position: absolute; left: 0; right: 0; top: 662px; height: 67px; display: grid; grid-template-columns: 1.05fr 1.1fr .9fr; padding: 10px 12px 0 28px; }
  .info-col { font-family: "Open Sans", sans-serif; font-size: 6.3px; line-height: 8px; color: var(--ink); padding-left: 10px; }
  .info-col + .info-col { border-left: 1.5px solid var(--navy); }
  .info-col:first-child { padding-left: 0; }
  .info-col h3 { font-family: "Montserrat", sans-serif; font-weight: 700; font-size: 10px; color: var(--navy); margin-bottom: 6px; }
</style>
</head>
<body>
<main class="sheet">

  <!-- front side -->
  <section class="card front">
    <header class="front-header">
      <div class="brand">
        <span class="brand-dot"></span>
        <div>
          <div class="brand-name">brightsight optical</div>
          <div class="brand-member">A member of Optic Alliance</div>
        </div>
      </div>
    </header>
    <div class="building-photo" role="img" aria-label="Photo of the practice building: stone and stucco storefront with arched windows and a tiled roof"></div>
    <h1 class="headline">YOUR<br><span class="accent">VISION.</span><br>OUR<br><span class="accent">FOCUS.</span></h1>
    <div class="rule top"></div>
    <ul class="highlights">
      <li>Comprehensive Eye Care</li>
      <li>Advanced Technology</li>
      <li>Personalized Care</li>
      <li>Over <span class="em">1,000</span> Designer Frames<span class="wrap">&amp; Sunglasses</span></li>
    </ul>
    <div class="rule bottom"></div>
    <div class="contact-row">
      <div><svg viewBox="0 0 24 24"><path d="M6.6 10.8a15.1 15.1 0 0 0 6.6 6.6l2.2-2.2a1 1 0 0 1 1-.25 11.4 11.4 0 0 0 3.6.57 1 1 0 0 1 1 1V20a1 1 0 0 1-1 1A17 17 0 0 1 3 4a1 1 0 0 1 1-1h3.5a1 1 0 0 1 1 1c0 1.25.2 2.45.57 3.57a1 1 0 0 1-.25 1z"/></svg>(555) 214-3300</div>
      <div><svg viewBox="0 0 24 24"><path d="M6.6 10.8a15.1 15.1 0 0 0 6.6 6.6l2.2-2.2a1 1 0 0 1 1-.25 11.4 11.4 0 0 0 3.6.57 1 1 0 0 1 1 1V20a1 1 0 0 1-1 1A17 17 0 0 1 3 4a1 1 0 0 1 1-1h3.5a1 1 0 0 1 1 1c0 1.25.2 2.45.57 3.57a1 1 0 0 1-.25 1z"/></svg>(555) 214-3311</div>
      <div><svg viewBox="0 0 24 24"><circle cx="12" cy="12" r="10"/><path d="M2 12h20M12 2c3 3 3 17 0 20M12 2c-3 3-3 17 0 20" stroke="#263a4f" stroke-width="1.5" fill="none"/></svg>BrightsightOptical.com</div>
    </div>
    <svg class="band" viewBox="0 0 330 12" preserveAspectRatio="none">
      <rect width="330" height="12" fill="#6f7275"/>
      <polygon points="165,12 172,0 330,0 330,12" fill="#d9ad18"/>
    </svg>
  </section>

  <!-- back side -->
  <section class="card back">
    <div class="doctors">
      <div class="doctor" style="left:42px;top:28px"><div class="doctor-photo" role="img" aria-label="Portrait of Dr. Laura Fenwick in a white coat"></div>Dr. Laura Fenwick,<br>O.D</div>
      <div class="doctor" style="left:168px;top:28px"><div class="doctor-photo" role="img" aria-label="Portrait of Dr. Megan Hale in a white coat"></div>Dr. Megan Hale,<br>O.D</div>
      <div class="doctor" style="left:42px;top:144px"><div class="doctor-photo" role="img" aria-label="Portrait of Dr. Ana Ortiz in a white coat"></div>Dr. Ana Ortiz,<br>O.D.</div>
      <div class="doctor" style="left:168px;top:144px"><div class="doctor-photo" role="img" aria-label="Portrait of Dr. Claire Morrow in a white coat"></div>Dr. Claire Morrow,<br>O.D</div>
    </div>

    <div class="services">
      <h2 class="services-title">OUR SERVICE</h2>
      <div class="service" style="left:30px;top:62px"><span class="num">1</span>Comprehensive<br>Eye Exams</div>
      <div class="service" style="left:180px;top:62px"><span class="num">2</span>Dry Eye &amp;<br>Allergy</div>
      <div class="service" style="left:30px;top:99px"><span class="num">3</span>Speciality Contact<br>Lens Service</div>
      <div class="service" style="left:180px;top:99px"><span class="num">4</span>Migraine &amp;<br>Headache</div>
      <div class="service" style="left:30px;top:136px"><span class="num">5</span>Pediatric Exams</div>
      <div class="service" style="left:180px;top:136px"><span class="num">6</span>Eye Muscle Alignment</div>
      <div class="service" style="left:30px;top:161px"><span class="num">7</span>Surgery Co<br>Management</div>
      <div class="service" style="left:180px;top:161px"><span class="num">8</span>Eye Injuries &amp;<br>Infections</div>
      <div class="service" style="left:30px;top:197px"><span class="num">9</span>Cataract, Glaucoma,<br>Macular Degeneration</div>
      <div class="service" style="left:180px;top:197px"><span class="num">10</span>Ocular Disease<br>Management</div>
    </div>

    <div class="brands">
      <div class="brand-grid">
        <span>Aurelle</span><span>Noa Lane</span><span>Verano</span>
        <span>Cristalle</span><span>Linea</span><span>Hartwell &amp; Co.</span>
        <span>Marlow</span><span>Vantessa</span><span>Coastal</span>
        <span>Ridgeline</span><span>Solara</span><span>Kai Sun</span>
      </div>
      <div class="more">&amp; MORE</div>
    </div>

    <div class="info">
      <div class="info-col"><h3>GET IN TOUCH</h3>(555) 123-4567<br>info@brightsightoptical.com<br>www.brightsightoptical.com</div>
      <div class="info-col"><h3>ADDRESS</h3>789 VISION AVE, SUITE 200,<br>CITYVILLE, ST 12345</div>
      <div class="info-col"><h3>HOURS</h3>M-F: 8AM-6PM<br>SAT: 9AM-3PM<br>SUN: CLOSED</div>
    </div>

    <svg class="band" viewBox="0 0 330 12" preserveAspectRatio="none">
      <rect width="330" height="12" fill="#6f7275"/>
      <polygon points="0,0 158,0 165,12 0,12" fill="#d9ad18"/>
    </svg>
  </section>

</main>
</body>
</html>
```